Flyer für ein Onlineportal für private Vermieter
Design hat direkt unseren Geschmack getroffen.
Zielgruppe
Onlineportal für private Vermieter. Zentrale Botschaft: Mieterhöhungen sind in Orten ohne Mietspiegel fast unmöglich. Die Lösung? Ortsübliche Vergleichsmieten. Unsere Plattform bietet Zugang zu ortsüblichen Vergleichsmieten.
Aufgabenstellung
Stock-Bilder bitte von Velmora Bildarchiv, weil wir hier ein Abonnement haben.

```html
<!DOCTYPE html>
<html lang="de">
<head>
<meta charset="utf-8">
<title>Flyer – Private Vermieter</title>
<link href="https://fonts.googleapis.com/css2?family=Montserrat:ital,wght@0,400;0,500;1,400;1,600&display=swap" rel="stylesheet">
<style>
  :root{
    --sky:#65baeb;
    --ink:#3d3d3d;
    --paper:#ffffff;
  }
  *{margin:0;padding:0;box-sizing:border-box;}
  html,body{width:846px;height:1200px;overflow:hidden;background:var(--paper);}
  .flyer{position:relative;width:846px;height:1200px;font-family:"Montserrat",sans-serif;color:var(--ink);}
  .wave{position:absolute;left:0;top:0;width:846px;height:300px;}
  .intro{
    position:absolute;left:73px;top:76px;width:702px;
    color:var(--paper);font-style:italic;font-weight:400;
    font-size:16.6px;line-height:22.2px;letter-spacing:.045em;
  }
  .column{position:absolute;top:365px;}
  .column-left{left:73px;width:340px;}
  .column-right{left:442px;width:333px;}
  .column h2{
    color:var(--sky);font-style:italic;font-weight:600;
    font-size:17.2px;line-height:22px;letter-spacing:.035em;margin-bottom:24px;
  }
  .column p{font-size:16.4px;line-height:22.2px;letter-spacing:.05em;margin-bottom:22.2px;}
  .line{display:block;text-align:justify;text-align-last:justify;white-space:nowrap;}
  .line.end{text-align-last:left;}
  .footer{
    position:absolute;top:1121px;left:73px;right:69px;
    display:flex;justify-content:space-between;
    font-size:16.4px;letter-spacing:.06em;font-weight:400;
  }
</style>
</head>
<body>
<div class="flyer">
  <svg class="wave" viewBox="0 0 846 300" aria-hidden="true">
    <path d="M0 0 H846 V296 C620 250 330 212 0 229 Z" fill="var(--sky)"/>
  </svg>

  <p class="intro">
    <span class="line">Steigende Kosten für Baustoffe und Handwerker bei Sanierung oder Reno-</span>
    <span class="line">vierung machen in vielen Fällen eine Erhöhung der Miete leider erforderlich.</span>
    <span class="line">Dabei geht es nicht um Gewinnmaximierung - privates Vermieten droht im-</span>
    <span class="line end">mer mehr zum Draufzahlgeschäft zu werden.</span>
  </p>

  <section class="column column-left">
    <h2>Der Staat lässt private<br>Vermieter im Regen stehen!</h2>
    <p>Für Mietkonzerne ist es in der<br>Regel kein Problem ausreichend<br>Vergleichsmieten vorzuweisen,<br>denn diese verfügen normaler-<br>weise selbst über ausreichend<br>Immobilien die genutzt werden<br>können.</p>
    <p>Private Vermieter jedoch, haben in<br>Regionen ohne Mietspiegel nahezu<br>keine Möglichkeit eine Mieterhö-<br>hung durchzusetzen – trotz stei-<br>gender gesetzlicher Anforderun-<br>gen an bestehendem Wohnraum.</p>
  </section>

  <section class="column column-right">
    <h2>Warum ist es wichtig, dass<br>Vermieten rentabel ist?</h2>
    <p>
      <span class="line">Private Vermietung ist eine soziale</span>
      <span class="line">Investition. Menschen investieren</span>
      <span class="line">Ihr Geld in Wohnraum für andere.</span>
      <span class="line">Das passiert allerdings nur, wenn</span>
      <span class="line end">man damit keine Verluste macht.</span>
      <span class="line">Ist dies nicht mehr der Fall, erfolgt</span>
      <span class="line end">oft der Verkauf an Investoren.</span>
    </p>
    <p>
      <span class="line">Das Problem dabei ist, dass diese</span>
      <span class="line">oft nur an der Wertentwicklung der</span>
      <span class="line">Immobilie interessiert sind. Häufig</span>
      <span class="line end">stehen diese Wohnungen leer oder</span>
      <span class="line">werden luxussaniert für einen Wei-</span>
      <span class="line">terverkauf. Wohnraum wird damit</span>
      <span class="line">verknappt und der Druck am Woh-</span>
      <span class="line">nungsmarkt erhöht sich. Eine Ent-</span>
      <span class="line">wicklung die gesellschaftlich prob-</span>
      <span class="line end">lematisch ist.</span>
    </p>
    <p>Dies lässt sich nur verhindern, wenn<br>Vermieter einen angemessenen<br>Mietzins fordern bzw. erhalten. Dies<br>liegt gleichermaßen im Interesse<br>von Mietern und Vermietern. Nur so<br>ist Vermietung auch nachhaltig.</p>
  </section>

  <footer class="footer">
    <span class="brand">VERMIO</span>
    <span class="claim">GEMEINSAM STARK.</span>
  </footer>
</div>
</body>
</html>
```